Business card design needed

Design:
Want the logo/design to have an enviromental feel
Simple look not to busy

Company Info:
Pre purchase building and pest inspections
Registered building practitoner DB-U 58147 (please include building commission logo in design)

Industry/Entity Type

Building

Contact Information for Business Card

Company name:
Fernvale Building and Pest inspections

Inspectors:
Dean Harker 0451 278 914
Greg Sutcliffe 0419 562 843
Email: fernvalebpi@mailpost.example

```html
<!DOCTYPE html>
<html lang="en">
<head>
<meta charset="utf-8">
<title>Fernvale Building and Pest Inspections – Business Card</title>
<link rel="stylesheet" href="https://fonts.googleapis.com/css2?family=Arimo:wght@400;700&display=swap">
<style>
  :root {
    --navy: #2a3e5a;
    --ink: #2a3f5c;
    --paper: #ffffff;
    --edge: #d9dde2;
    --sky: #6cc3ef;
    --white: #ffffff;
    --arc-top: #16c1f2;
    --arc-bottom: #0a62a8;
  }
  html, body {
    margin: 0;
    padding: 0;
    width: 1200px;
    height: 667px;
    overflow: hidden;
    background: var(--paper);
  }
  .card {
    position: relative;
    width: 1200px;
    height: 667px;
    overflow: hidden;
    border-radius: 38px;
    box-sizing: border-box;
    border: 1px solid var(--edge);
    background: var(--paper);
    font-family: "Arimo", Arial, sans-serif;
  }
  .card-shapes {
    position: absolute;
    inset: 0;
    width: 100%;
    height: 100%;
  }
  .brand-name {
    position: absolute;
    left: 95px;
    width: 360px;
    top: 330px;
    margin: 0;
    text-align: center;
    font-family: "Arimo", Arial, sans-serif;
    font-weight: 700;
    font-size: 32px;
    line-height: 40px;
    color: var(--ink);
  }
  .contacts {
    position: absolute;
    right: 88px;
    top: 238px;
    text-align: right;
  }
  .contacts-title {
    margin: 0 0 6px;
    font-size: 30px;
    font-weight: 700;
    color: var(--sky);
    line-height: 1.1;
  }
  .contacts-list {
    margin: 0;
    padding: 0;
    list-style: none;
    font-size: 22px;
    line-height: 29px;
    color: var(--white);
  }
  .services {
    position: absolute;
    right: 88px;
    top: 573px;
    margin: 0;
    text-align: right;
    font-size: 21.5px;
    line-height: 28px;
    color: var(--sky);
  }
</style>
</head>
<body>
  <main class="card">
    <svg class="card-shapes" viewBox="0 0 1243 691" preserveAspectRatio="none" aria-hidden="true">
      <defs>
        <linearGradient id="arcGradient" x1="0" y1="0" x2="0" y2="1">
          <stop offset="0" stop-color="var(--arc-top)"/>
          <stop offset="1" stop-color="var(--arc-bottom)"/>
        </linearGradient>
      </defs>
      <path class="navy-panel" d="M505 0 Q831 345.5 505 691 L1243 691 L1243 0 Z" fill="var(--navy)"/>
      <path class="accent-arc" d="M512 14 Q792 345.5 512 677 Q745 345.5 512 14 Z" fill="url(#arcGradient)"/>
    </svg>

    <h1 class="brand-name">Fernvale Building and Pest inspections</h1>

    <section class="contacts">
      <h2 class="contacts-title">Inspectors:</h2>
      <ul class="contacts-list">
        <li>Dean Harker - 0451 278 914</li>
        <li>Greg Sutcliffe - 0419 562 843</li>
        <li>Email : fernvalebpi@mailpost.example</li>
      </ul>
    </section>

    <p class="services">
      Pre purchase building and pest inspections<br>
      Registered building practitoner DB-U 58147
    </p>
  </main>
</body>
</html>
```